Online ticketing company needs new biz card design

Needing an updated business card to reflect our company, incorporating our existing logo and colour scheme (red, black, white). The design should communicate our modern, online, technology, innovation based company.

Details for card need to include the following:

Name
Position
Telephone and extension number
Mobile number
Email
Web address
Physical and/or postal address

Industry/Entity Type

Business

Font styles to use
Sans Serif

Requirements
Must have
• Clear, bold, eye catching design

```html
<!DOCTYPE html>
<html lang="en">
<head>
<meta charset="utf-8">
<title>Stubline Business Card</title>
<link rel="stylesheet" href="https://fonts.googleapis.com/css2?family=Exo+2:wght@400;500;700;800&display=swap">
<style>
  :root {
    --stage: #b9bbbe;
    --red: #d11f2b;
    --red-deep: #a8141f;
    --black: #121212;
    --black-soft: #262626;
    --white: #ffffff;
    --grey-text: #d8d8d8;
  }
  * { box-sizing: border-box; margin: 0; padding: 0; }
  html, body {
    width: 1200px; height: 800px; overflow: hidden;
    background: var(--stage);
    font-family: "Exo 2", sans-serif;
  }
  .stage { position: relative; width: 1200px; height: 800px; }

  /* Front card */
  .card-front {
    position: absolute; left: 110px; top: 120px;
    width: 340px; height: 560px;
    background: var(--red);
    overflow: hidden;
  }
  .card-front .texture {
    position: absolute; inset: 0;
    background: radial-gradient(ellipse at 60% 20%, #e0303b 0%, var(--red) 45%, var(--red-deep) 100%);
  }
  .card-front .edge-bands { position: absolute; inset: 0; }
  .card-front .brand {
    position: absolute; left: 0; right: 0; top: 50%;
    transform: translateY(-50%);
    text-align: center;
    font-weight: 800; font-size: 46px; letter-spacing: 1px;
    color: var(--black);
  }

  /* Back card */
  .card-back {
    position: absolute; left: 500px; top: 230px;
    width: 595px; height: 340px;
    background: var(--black);
    overflow: hidden;
  }
  .card-back .texture {
    position: absolute; inset: 0;
    background: radial-gradient(ellipse at 40% 50%, var(--black-soft) 0%, var(--black) 70%);
  }
  .card-back .corner-band { position: absolute; inset: 0; }
  .card-back .brand {
    position: absolute; left: 40px; top: 125px;
    font-weight: 800; font-size: 44px; letter-spacing: 1px;
    color: var(--white);
  }
  .card-back .anniversary-badge {
    position: absolute; left: 150px; top: 185px;
    width: 46px; height: 46px; border-radius: 50%;
    background: var(--red); border: 3px solid var(--white);
  }
  .contact {
    position: absolute; left: 330px; top: 70px;
    color: var(--red);
  }
  .contact .person-name {
    font-weight: 700; font-size: 26px; text-transform: uppercase; letter-spacing: .5px;
    line-height: 1;
  }
  .contact .person-role {
    color: var(--white); font-size: 15px; margin: 4px 0 14px;
  }
  .contact ul { list-style: none; font-size: 14px; line-height: 20px; }
  .contact li { display: flex; align-items: center; gap: 8px; }
  .contact li svg { width: 11px; height: 11px; flex: none; fill: var(--white); }
  .contact .ext { color: var(--white); }
  .contact .address { margin-top: 10px; }
  .contact .address li { align-items: flex-start; }
  .contact .address li svg { margin-top: 4px; }
  .contact .address .spacer { width: 11px; flex: none; }
</style>
</head>
<body>
<main class="stage">

  <section class="card-front" aria-label="Card front">
    <div class="texture" role="img" aria-label="Red diamond pixel pattern background"></div>
    <svg class="edge-bands" viewBox="0 0 340 560" preserveAspectRatio="none" aria-hidden="true">
      <polygon points="0,0 22,0 22,250 34,262 34,298 22,310 22,560 0,560" fill="var(--black)"/>
      <polygon points="340,0 318,0 318,250 306,262 306,298 318,310 318,560 340,560" fill="var(--black)"/>
    </svg>
    <div class="brand">STUBLINE</div>
  </section>

  <section class="card-back" aria-label="Card back">
    <div class="texture" role="img" aria-label="Dark diamond pixel pattern background"></div>
    <svg class="corner-band" viewBox="0 0 595 340" preserveAspectRatio="none" aria-hidden="true">
      <polygon points="0,0 260,0 245,14 0,14" fill="var(--red)"/>
    </svg>
    <div class="brand">STUBLINE</div>
    <div class="anniversary-badge"></div>

    <div class="contact">
      <p class="person-name">Hana Verity</p>
      <p class="person-role">Customer Support</p>
      <ul>
        <li><svg viewBox="0 0 12 12"><path d="M2 1h3l1 3-2 1a7 7 0 0 0 3 3l1-2 3 1v3c0 1-1 1-1 1A10 10 0 0 1 1 2c0 0 0-1 1-1z"/></svg>0800 STUBLN <span class="ext">(xx)</span></li>
        <li><svg viewBox="0 0 12 12"><path d="M3 0h6v12H3z M4 1v8h4V1z"/></svg>021 555 0148</li>
        <li><svg viewBox="0 0 12 12"><path d="M0 2h12v8H0z M1 3l5 4 5-4v-.01H1z" fill-rule="evenodd"/></svg>help@stubline.co.nz</li>
        <li><svg viewBox="0 0 12 12"><path d="M6 0a6 6 0 1 0 0 12A6 6 0 0 0 6 0zm0 1.2c.8 1 1.3 2.4 1.4 4.2H4.6C4.7 3.6 5.2 2.2 6 1.2zM1.3 6.6h2.3c.1 1.7.6 3 1.2 4.1A4.8 4.8 0 0 1 1.3 6.6zm0-1.2a4.8 4.8 0 0 1 3.5-4.1c-.6 1.1-1.1 2.4-1.2 4.1zm4.7 5.4c-.8-1-1.3-2.4-1.4-4.2h2.8c-.1 1.8-.6 3.2-1.4 4.2zm1.2-.1c.6-1.1 1.1-2.4 1.2-4.1h2.3a4.8 4.8 0 0 1-3.5 4.1zm1.2-5.3c-.1-1.7-.6-3-1.2-4.1a4.8 4.8 0 0 1 3.5 4.1z"/></svg>www.stubline.co.nz</li>
      </ul>
      <ul class="address">
        <li><svg viewBox="0 0 12 12"><path d="M6 0l6 6h-2v6H2V6H0z"/></svg>PO Box 18240, Kingsland</li>
        <li><span class="spacer"></span>Auckland</li>
        <li><span class="spacer"></span>New Zealand</li>
      </ul>
    </div>
  </section>

</main>
</body>
</html>
```